V STUDIO Interior & Exterior Designer Business needs a Business Card

V STUDIO - I need a Business Card Design for a Interior Design Business, I work Nationally Around Australia on Projects specialising In AGED CARE and would like to rebrand and change the Look.
I work mainly with Large Corporate Companys, Select everything From External Finishes to All Internal Finishes, Furniture and then Decorate to a 5 star finish.

Industry/Entity Type

Business

Contact Information for Business Card

V STUDIO
Marlene Oberly
PH: (+61) 0400 982 637
E: marly@vstudioinclub.com

Font styles to use
Sans Serif

Requirements
Must have
• My Priject Must Have a Contemporary Design, Bold, Eye Catching, that makes a statement but MUST BE ELEGANT - 2 or 3 Colours - Strong Power Colours.
• 2 sided
• i like the works - IMAGEN, DESIGN, CREATE
Nice to have
• I would like the words ' envision shape inspire ' incorporated into the design
• I like Some Red on the card

```html
<!DOCTYPE html>
<html lang="en">
<head>
<meta charset="utf-8">
<title>V STUDIO – Business Card</title>
<link rel="stylesheet" href="https://fonts.googleapis.com/css2?family=Arimo:wght@400&family=Questrial&display=swap">
<style>
  :root {
    --backdrop: #e9e9e9;
    --card: #ffffff;
    --power-red: #ec1c24;
    --chevron-grey: #d2d2d2;
    --ink: #1a1a1a;
    --tagline-pink: #ef5ba1;
    --wordmark-pink: #e8336f;
    --icon-grey: #222222;
  }
  * { box-sizing: border-box; margin: 0; padding: 0; }
  html, body {
    width: 1126px; height: 1200px; overflow: hidden;
    background: var(--backdrop);
    font-family: "Arimo", Arial, sans-serif;
    color: var(--ink);
  }
  .sheet {
    position: relative; width: 1126px; height: 1200px;
    display: flex; flex-direction: column; align-items: center;
    justify-content: center; gap: 56px;
  }
  .card {
    position: relative; width: 860px; height: 484px;
    background: var(--card);
    box-shadow: 0 2px 10px rgba(0,0,0,.12);
    overflow: hidden;
  }
  /* Front */
  .card-front .chevron { position: absolute; left: 0; top: 0; width: 352px; height: 484px; }
  .card-front .details { position: absolute; left: 385px; top: 40px; }
  .person-name { font-size: 37px; color: var(--power-red); line-height: 1; }
  .phone { display: flex; align-items: center; gap: 12px; margin-top: 14px; font-size: 26px; }
  .studio-name {
    font-family: "Questrial", "Century Gothic", sans-serif;
    font-size: 72px; letter-spacing: 1px; line-height: 1; margin-top: 52px;
    color: var(--ink);
  }
  .tagline { font-size: 30px; color: var(--tagline-pink); margin-top: 4px; }
  .address { font-size: 22px; margin-top: 26px; line-height: 1.35; }
  .contact-line { display: flex; align-items: center; gap: 8px; font-size: 22px; line-height: 1.35; }
  .icon { width: 20px; height: 20px; flex: none; }
  /* Back */
  .card-back .lockup {
    position: absolute; left: 0; right: 0; top: 176px;
    display: flex; flex-direction: column; align-items: center;
  }
  .card-back .studio-name { margin-top: 0; font-size: 84px; color: var(--wordmark-pink); }
  .card-back .tagline { color: var(--ink); font-size: 32px; margin-top: 6px; }
</style>
</head>
<body>
<main class="sheet">

  <section class="card card-front" aria-label="Business card front">
    <svg class="chevron" viewBox="0 0 352 484" aria-hidden="true">
      <polygon points="0,0 109,0 352,242 109,484 0,484" fill="var(--chevron-grey)"/>
      <polygon points="0,0 296,242 0,484" fill="var(--power-red)"/>
      <circle cx="150" cy="242" r="34" fill="#ffffff"/>
    </svg>
    <div class="details">
      <p class="person-name">Marlene Oberly</p>
      <p class="phone">
        <svg class="icon" viewBox="0 0 20 20" aria-hidden="true">
          <rect x="2" y="0" width="16" height="20" rx="3" fill="var(--tagline-pink)"/>
          <rect x="6" y="3" width="8" height="12" rx="1" fill="#fff"/>
        </svg>
        (+61) 0400 982 637
      </p>
      <p class="studio-name">V STUDIO</p>
      <p class="tagline">envision shape inspire</p>
      <p class="address">218 Harbour View Rd | PMB #2207<br>AUSTRALIA</p>
      <p class="contact-line">
        <svg class="icon" viewBox="0 0 20 20" aria-hidden="true">
          <rect x="1" y="4" width="18" height="12" rx="2" fill="var(--icon-grey)"/>
          <polyline points="3,6 10,11 17,6" fill="none" stroke="#fff" stroke-width="1.6"/>
        </svg>
        marly@vstudioinclub.com
      </p>
      <p class="contact-line">
        <svg class="icon" viewBox="0 0 20 20" aria-hidden="true">
          <rect x="1" y="1" width="18" height="18" rx="3" fill="var(--icon-grey)"/>
          <circle cx="10" cy="10" r="6" fill="none" stroke="#fff" stroke-width="1.3"/>
          <line x1="4" y1="10" x2="16" y2="10" stroke="#fff" stroke-width="1.2"/>
          <ellipse cx="10" cy="10" rx="2.6" ry="6" fill="none" stroke="#fff" stroke-width="1.2"/>
        </svg>
        www.marlyvstudioaust.com
      </p>
    </div>
  </section>

  <section class="card card-back" aria-label="Business card back">
    <div class="lockup">
      <p class="studio-name">V STUDIO</p>
      <p class="tagline">envision shape inspire</p>
    </div>
  </section>

</main>
</body>
</html>
```